Security Company Needs an UPDATED Business Card and Letterhead Design!

I run a security company and would like to have an updated BUSINESS CARD + LETTERHEAD DESIGN.

Please use my UPDATED address below:

2875 E. Thornwick Road
Suite 614 Dallas, Texas 75390

Attached is the current business card as reference, and also my logo.

Target Market(s)

High end security users such as Class A buildings, Corporate Campus Locations, Hospitals, High End Retail Centers, Warehousing, Manufacturing and High Tech Companies

Industry/Entity Type

Security Guard

Contact Information for Business Card

Looking for unique, yet professional

Requirements
Must have
• Must use the current logo and incorporate it into any design. Use the colors that are included in the logo. I also need to be able to easily add employees as the company grows. Should be an easy process to change Names and Numbers

```html
<!DOCTYPE html>
<html lang="en">
<head>
<meta charset="utf-8">
<title>Hollins Guard Group – Business Card</title>
<link href="https://fonts.googleapis.com/css2?family=Open+Sans:wght@400;600;700&display=swap" rel="stylesheet">
<style>
  :root{
    --backdrop:#e9e6e1;
    --card-white:#ffffff;
    --panel-light:#dcdce1;
    --panel-dark:#a7a7b0;
    --brand-navy:#2f2a80;
    --text-light:#ffffff;
    --icon-ink:#2f2a80;
  }
  *{box-sizing:border-box;margin:0;padding:0}
  html,body{width:1200px;height:1022px;overflow:hidden}
  body{background:var(--backdrop);font-family:"Open Sans",Arial,sans-serif;position:relative}
  .card{
    position:absolute;left:120px;top:231px;width:960px;height:560px;
    background:var(--card-white);border-radius:22px;overflow:hidden;
    box-shadow:0 14px 40px rgba(0,0,0,.18);
  }
  .card-panel{position:absolute;inset:0;width:960px;height:560px}
  .contact{
    position:absolute;left:60px;top:96px;color:var(--text-light);
  }
  .contact-name{
    font-weight:700;font-size:40px;letter-spacing:1px;color:var(--brand-navy);
    text-transform:uppercase;line-height:1.1;
  }
  .contact-title{
    font-weight:700;font-size:19px;letter-spacing:1.5px;text-transform:uppercase;
    margin-top:6px;
  }
  .contact-address{font-size:21px;line-height:1.45;margin-top:28px;font-weight:600}
  .contact-lines{list-style:none;margin-top:20px;font-size:21px;font-weight:600;line-height:1.45}
  .contact-lines li{display:flex;align-items:center;gap:14px}
  .contact-lines svg{width:18px;height:18px;flex:none}
  .brand{
    position:absolute;left:640px;top:230px;display:flex;align-items:center;gap:16px;
  }
  .brand-dot{width:54px;height:54px;border-radius:50%;background:var(--brand-navy)}
  .brand-name{
    font-weight:700;font-size:28px;line-height:1.15;color:var(--brand-navy);
    text-transform:uppercase;letter-spacing:1px;
  }
</style>
</head>
<body>
  <div class="card">
    <svg class="card-panel" viewBox="0 0 960 560" aria-hidden="true">
      <defs>
        <linearGradient id="panelShade" x1="0" y1="0" x2="1" y2="1">
          <stop offset="0" stop-color="var(--panel-dark)"/>
          <stop offset="0.55" stop-color="var(--panel-light)"/>
          <stop offset="1" stop-color="var(--panel-dark)"/>
        </linearGradient>
      </defs>
      <path d="M0 0 H520 Q640 280 520 560 H0 Z" fill="url(#panelShade)"/>
      <path d="M520 0 Q640 280 520 560" fill="none" stroke="var(--brand-navy)" stroke-width="4"/>
    </svg>

    <div class="contact">
      <p class="contact-name">Marcus D. Hollins</p>
      <p class="contact-title">President &amp; CEO</p>
      <p class="contact-address">2875 E. Thornwick Road<br>Suite 614 Dallas, Texas 75390</p>
      <ul class="contact-lines">
        <li>
          <svg viewBox="0 0 20 20"><path d="M5 2l3 4-2 2c1 2 3 4 5 5l2-2 4 3-2 3C9 17 3 11 2 4z" fill="var(--icon-ink)"/></svg>
          602-555-0187
        </li>
        <li>
          <svg viewBox="0 0 20 20"><rect x="2" y="4" width="16" height="12" fill="none" stroke="var(--icon-ink)" stroke-width="2"/><path d="M2 4l8 7 8-7" fill="none" stroke="var(--icon-ink)" stroke-width="2"/></svg>
          marcus@hollinsguardgroup.com
        </li>
        <li>
          <svg viewBox="0 0 20 20"><circle cx="10" cy="10" r="8" fill="none" stroke="var(--icon-ink)" stroke-width="2"/><path d="M2 10h16M10 2c-4 5-4 11 0 16M10 2c4 5 4 11 0 16" fill="none" stroke="var(--icon-ink)" stroke-width="1.5"/></svg>
          www.hollinsguard.com
        </li>
        <li>
          <svg viewBox="0 0 20 20"><circle cx="10" cy="10" r="8" fill="var(--icon-ink)"/></svg>
          www.profilelink.com/in/mdhollins
        </li>
      </ul>
    </div>

    <div class="brand">
      <span class="brand-dot"></span>
      <span class="brand-name">Hollins<br>Guard Group</span>
    </div>
  </div>
</body>
</html>
```